Vurlo App

We want to have a web banner (4-5 slides) flash or whatever.
We are innovative next generation messenger with a good design, themes, snap mode, pinging and other features.
Inspired by night, by techno music, by energy, by innovations and next generation.
High tech.

The name of the app : Vurlo
vurloapp.example

The banner will be used for nightdeckmag.example

We want the banner to be creative, and deliver the inspiration of the app.

All the assets, logos and so on can me delivered to you via email by request.

```html
<!DOCTYPE html>
<html lang="en">
<head>
<meta charset="utf-8">
<title>Vurlo – Inspired by night</title>
<link href="https://fonts.googleapis.com/css2?family=Montserrat:wght@500;600;700&display=swap" rel="stylesheet">
<style>
  :root {
    --page-bg: #525c65;
    --banner-border: #e8eef2;
    --night-teal: #1f6f7a;
    --night-green: #2f7d22;
    --deep-green: #1c4a12;
    --leaf-green: #6fbf2a;
    --ember-orange: #e08a1e;
    --text-light: #ffffff;
    --button-top: #a9e6ff;
    --button-bottom: #3fb0ea;
    --button-edge: #e9f8ff;
    --button-text: #0d2a3a;
    --mark-blue: #5bbcf5;
  }
  * { margin: 0; padding: 0; box-sizing: border-box; }
  html, body { width: 1200px; height: 900px; overflow: hidden; }
  body {
    background: var(--page-bg);
    font-family: "Montserrat", Arial, sans-serif;
    position: relative;
  }
  .banner {
    position: absolute;
    left: 52px; top: 381px;
    width: 1096px; height: 138px;
    border: 2px solid var(--banner-border);
    overflow: hidden;
  }
  .banner-art {
    position: absolute; inset: 0;
    background:
      radial-gradient(ellipse 35% 120% at 50% 60%, var(--deep-green) 0%, transparent 70%),
      linear-gradient(100deg, var(--night-teal) 0%, var(--night-green) 25%, var(--leaf-green) 42%, var(--night-green) 58%, #4f7a1a 75%, var(--ember-orange) 100%);
  }
  .brand {
    position: absolute;
    left: 20px; top: 20px;
    display: flex; align-items: center; gap: 30px;
  }
  .brand-square {
    width: 96px; height: 90px;
    border-radius: 8px;
    background: var(--mark-blue);
  }
  .brand-name {
    color: var(--text-light);
    font-weight: 700;
    font-size: 50px;
    letter-spacing: -0.5px;
  }
  .message {
    position: absolute;
    left: 346px; top: 6px;
    color: var(--text-light);
  }
  .headline {
    font-weight: 700;
    font-size: 50px;
    line-height: 66px;
    letter-spacing: -0.3px;
  }
  .subline {
    font-weight: 600;
    font-size: 22px;
    line-height: 32px;
  }
  .cta {
    position: absolute;
    left: 863px; top: 35px;
    width: 206px; height: 70px;
    border: 2px solid var(--button-edge);
    border-radius: 9px;
    background: linear-gradient(var(--button-top), var(--button-bottom));
    color: var(--button-text);
    font-family: inherit;
    font-weight: 500;
    font-size: 26px;
    display: flex; align-items: center; justify-content: center;
    box-shadow: 0 2px 4px rgba(0,0,0,0.3);
  }
</style>
</head>
<body>
  <section class="banner">
    <div class="banner-art" role="img" aria-label="Night-time abstract backdrop of green light rays, glowing bokeh dots and orange light streaks"></div>
    <div class="brand">
      <div class="brand-square"></div>
      <span class="brand-name">vurlo</span>
    </div>
    <div class="message">
      <h1 class="headline">Inspired by night!</h1>
      <p class="subline">New groundbreaking messenger<br>for your mobile now available!</p>
    </div>
    <div class="cta">Try it now!</div>
  </section>
</body>
</html>
```